Luxury Toilet Rental Business. Wavelet Hire.

Wavelet Hire (the logo is in the uploaded files)
We RENT and SELL Luxury Trailer toilets.
- Show location, number, pricing, pictures.
- We have two stall trailers for rent AND 3 stall trailers
- We sell them too
- We want our phone number shown
- We are a local company
- Slogan: Elevate your event with Wavelet Hire. The Luxurious Loo
- We want a pricing portion
- We want the sizes shown
- We want the different rates/ prices shown
- We do 1 day rentals
- We do 1 week rentals
- We want the service area. We serve Los Angeles County, Orange County, Riverside County, San Bernardino County, and Palm Desert.
- Our location is in Santa Ana California

Target Market(s)

Event planners, wedding planners, venue planners, concerts, events, gatherings.

Industry/Entity Type

Luxury Toilet Rentals

Number of Pages Required

1 page

Font styles to use
Serif
Sans Serif

Colors
EE7325
F08F49
F5BC92
FAE3D3
FDF4ED

Requirements
Must have
• Location, pricing, pictures, available areas. Our slogan.
Nice to have
• I like the idea of having tabs that show price, a tab that shows our contact information, pictures, event ideas, and where we service (the areas we'll go to)

```html
<!DOCTYPE html>
<html lang="en">
<head>
<meta charset="utf-8">
<title>Wavelet Hire — Luxury Restroom Trailers</title>
<link href="https://fonts.googleapis.com/css2?family=Krona+One&family=Poppins:wght@400;500;600&display=swap" rel="stylesheet">
<style>
:root{
  --orange:#ee7325;
  --orange-2:#f08f49;
  --peach:#f5bc92;
  --cream:#fdf4ed;
  --ink:#1a1a1a;
  --grey-text:#777;
  --panel:#f0f0f0;
  --white:#fff;
  --black:#000;
}
*{margin:0;padding:0;box-sizing:border-box}
html,body{width:1200px;height:3174px;overflow:hidden}
body{position:relative;background:var(--white);font-family:"Poppins",sans-serif;color:var(--ink)}
.abs{position:absolute}
.display{font-family:"Krona One",sans-serif}
.btn{position:absolute;display:flex;align-items:center;justify-content:center;font-family:"Krona One",sans-serif;font-size:10px;letter-spacing:.5px;color:var(--white);background:var(--orange)}
.btn.dark{background:var(--black)}
.logo{position:absolute;border:3px solid var(--orange);display:flex;align-items:center;justify-content:center;font-family:"Krona One",sans-serif;color:var(--orange)}
.social{position:absolute;width:14px;height:14px;border-radius:50%;border:2px solid currentColor}

.topbar{left:0;top:0;width:1200px;height:43px;background:var(--orange);color:var(--white);font-weight:500;font-size:16px}
.nav a{position:absolute;top:84px;font-family:"Krona One",sans-serif;font-size:13px;color:#444;text-decoration:none}
.hero{left:0;top:142px;width:1200px;height:555px;background:linear-gradient(90deg,#2e2f31 0%,#55585b 45%,#6b6e72 70%,#4d5054 100%)}
.hero h1{position:absolute;left:38px;top:150px;font-family:"Krona One",sans-serif;color:var(--white);font-size:33px;line-height:41px;font-weight:400}

.about-photo{left:58px;top:819px;width:531px;height:361px;border-radius:8px;background:linear-gradient(160deg,#b9b4a6,#8a8d90 55%,#6c6f73);z-index:2}
.about-block{left:330px;top:1008px;width:298px;height:207px;background:var(--orange);border-radius:8px}
.about h2{position:absolute;left:654px;top:844px;font-size:30px;font-weight:400}
.about p{position:absolute;left:654px;width:450px;font-size:10.5px;line-height:18.5px;color:var(--grey-text)}

.feature{position:absolute;top:1305px;width:300px;text-align:center}
.feature h3{font-family:"Krona One",sans-serif;font-size:22px;font-weight:400;margin-top:26px}
.feature p{font-size:10.5px;line-height:18.5px;color:var(--grey-text);margin-top:14px;padding:0 10px}

.trailers{left:0;top:1611px;width:1200px;height:735px;background:var(--panel)}
.section-title{position:absolute;left:0;width:1200px;text-align:center;font-family:"Krona One",sans-serif;font-weight:400;font-size:34px}
.card{position:absolute;top:1817px;width:329px;height:430px;background:var(--white);border-radius:32px}
.card .pic{position:absolute;left:55px;top:22px;width:219px;height:190px;border-radius:6px;background:linear-gradient(180deg,#6b6e72,#3f4246 75%,#2f7fb6)}
.card h4{position:absolute;left:0;top:228px;width:329px;text-align:center;font-size:21px;font-weight:500}
.card .spec{position:absolute;top:272px;font-size:14px;font-weight:600}
.card .spec span{font-weight:400;color:#999;margin-left:6px;font-size:13px}
.rates{position:absolute;left:21px;top:310px;width:287px;display:flex;background:var(--cream);border:1px solid var(--peach)}
.rate{flex:1;text-align:center;padding:7px 0}
.rate + .rate{border-left:1px solid var(--peach)}
.rate small{display:block;font-size:11px;color:var(--grey-text);font-weight:500;letter-spacing:.5px}
.rate b{font-size:18px;font-weight:600;color:var(--orange)}
.card .btn{top:378px;width:126px;height:27px}
.dot{position:absolute;top:2296px;width:84px;height:5px;background:var(--orange)}

.area{position:absolute;display:flex;align-items:center;gap:18px;font-size:21px;font-weight:500}
.tick{width:42px;height:42px;background:var(--orange);display:flex;align-items:center;justify-content:center}

.footer{left:0;top:2816px;width:1200px;height:358px;background:var(--black);color:var(--white)}
.footer h5{position:absolute;top:70px;font-family:"Krona One",sans-serif;font-weight:400;font-size:17px;color:var(--orange)}
.f-link{position:absolute;display:flex;align-items:center;gap:12px;font-size:17px;font-weight:500}
.f-tick{width:21px;height:21px;background:var(--orange);display:flex;align-items:center;justify-content:center}
</style>
</head>
<body>

<div class="abs topbar">
  <svg class="abs" style="left:38px;top:15px" width="16" height="12" viewBox="0 0 16 12"><rect width="16" height="12" fill="#fff"/><path d="M0 0l8 6 8-6" stroke="#ee7325" stroke-width="1.6" fill="none"/></svg>
  <span class="abs" style="left:70px;top:10px">info@website</span>
  <svg class="abs" style="left:282px;top:13px" width="16" height="16" viewBox="0 0 24 24"><path fill="#fff" d="M6.6 10.8a15 15 0 006.6 6.6l2.2-2.2c.3-.3.7-.4 1-.2 1.1.4 2.3.6 3.6.6.6 0 1 .4 1 1V20c0 .6-.4 1-1 1A17 17 0 013 4c0-.6.4-1 1-1h3.5c.6 0 1 .4 1 1 0 1.3.2 2.5.6 3.6.1.3 0 .7-.2 1z"/></svg>
  <span class="abs" style="left:312px;top:11px">123-456-7890</span>
  <span class="social" style="left:1060px;top:14px;color:#fff"></span>
  <span class="social" style="left:1102px;top:14px;color:#fff"></span>
  <span class="social" style="left:1146px;top:14px;color:#fff"></span>
</div>

<div class="logo" style="left:37px;top:62px;width:254px;height:58px;font-size:22px">Wavelet Hire</div>
<nav class="nav">
  <a style="left:363px">HOME</a>
  <a style="left:468px">ABOUT</a>
  <a style="left:590px">PRICES</a>
  <a style="left:706px">LOCATIONS</a>
  <a style="left:868px">EVENTS</a>
</nav>
<div class="btn" style="left:1018px;top:76px;width:146px;height:32px">CONTACT US</div>

<section class="abs hero" role="img" aria-label="Photo of a grey three-stall luxury restroom trailer with blue steps parked in a yard">
  <h1>Elevate your<br>event with<br>Wavelet Hire.<br>The Luxurious Loo</h1>
  <div class="btn" style="left:43px;top:356px;width:147px;height:33px">CONTACT US</div>
</section>

<section class="about">
  <div class="abs about-block"></div>
  <div class="abs about-photo" role="img" aria-label="Photo of a two-stall luxury restroom trailer with fold-out steps"></div>
  <h2 class="display">ABOUT US</h2>
  <p style="top:900px">Lorem ipsum dolor sit amet, consectetur adipiscing elit, sed do eiusmod tempor incididunt ut labore et dolore magna aliqua. Ut enim ad minim veniam, quis nostrud exercitation ullamco laboris nisi ut aliquip ex ea commodo consequat. Duis aute irure dolor in reprehenderit in voluptate velit esse cillum dolore eu fugiat nulla pariatur.</p>
  <p style="top:1001px">Lorem ipsum dolor sit amet, consectetur adipiscing elit, sed do eiusmod tempor incididunt ut labore et dolore magna aliqua. Ut enim ad minim veniam, quis nostrud exercitation ullamco laboris nisi ut aliquip ex ea commodo consequat. Duis aute irure dolor in reprehenderit in voluptate velit esse cillum dolore eu fugiat nulla pariatur.</p>
  <div class="btn" style="left:654px;top:1118px;width:147px;height:33px">READ MORE</div>
</section>

<div class="feature" style="left:96px">
  <svg width="74" height="74" viewBox="0 0 74 74" fill="none" stroke="#ee7325" stroke-width="2.5"><circle cx="20" cy="20" r="14"/><path d="M8 40h26l-5 12H13zM21 52v14M14 66h14"/><rect x="44" y="6" width="26" height="26"/><path d="M57 6v26M48 40h16v20H48z"/></svg>
  <h3>High-End</h3>
  <p>Lorem ipsum dolor sit amet, consectetur adipiscing elit, sed do eiusmod temporincididunt ut labore et dolore magna aliqua. Ut enim ad minim veniam, quis nostrud</p>
</div>
<div class="feature" style="left:439px">
  <svg width="80" height="74" viewBox="0 0 80 74" fill="none" stroke="#ee7325" stroke-width="2.5"><rect x="6" y="12" width="68" height="36"/><path d="M14 12v36M24 12v36M34 12v36M44 12v36M54 12v36M64 12v36M6 56h68"/><circle cx="40" cy="60" r="7"/><circle cx="54" cy="60" r="7"/></svg>
  <h3>Convenient</h3>
  <p>Lorem ipsum dolor sit amet, consectetur adipiscing elit, sed do eiusmod temporincididunt ut labore et dolore magna aliqua. Ut enim ad minim veniam, quis nostrud</p>
</div>
<div class="feature" style="left:806px">
  <svg width="74" height="74" viewBox="0 0 74 74" fill="none" stroke="#ee7325" stroke-width="2.5"><path d="M14 38h10v30H14zM24 40l10-14 4-14c4 0 6 4 5 10l-2 8h16c4 0 6 4 4 7l-4 20c-1 3-3 4-6 4H24"/><path d="M48 4v10M43 9h10M62 16v8M58 20h8M20 16v6M17 19h6"/></svg>
  <h3>Versatile</h3>
  <p>Lorem ipsum dolor sit amet, consectetur adipiscing elit, sed do eiusmod temporincididunt ut labore et dolore magna aliqua. Ut enim ad minim veniam, quis nostrud</p>
</div>

<section class="abs trailers"></section>
<h2 class="section-title" style="top:1678px">OUR TRAILERS</h2>

<div class="card" style="left:58px">
  <div class="pic" role="img" aria-label="Two-stall trailer product photo"></div>
  <h4>2 Stall Trailer</h4>
  <div class="spec" style="left:23px">SIZE : <span>144-1/2"</span></div>
  <div class="spec" style="left:160px">CONDITION : <span>New</span></div>
  <div class="rates"><div class="rate"><small>1 DAY</small><b>$450</b></div><div class="rate"><small>1 WEEK</small><b>$1,800</b></div></div>
  <div class="btn" style="left:21px">FOR RENT</div>
  <div class="btn dark" style="left:182px">BUY NOW</div>
</div>
<div class="card" style="left:442px">
  <div class="pic" role="img" aria-label="Three-stall trailer product photo"></div>
  <h4>3 Stall Trailer</h4>
  <div class="spec" style="left:23px">SIZE : <span>144-1/2"</span></div>
  <div class="spec" style="left:160px">CONDITION : <span>New</span></div>
  <div class="rates"><div class="rate"><small>1 DAY</small><b>$650</b></div><div class="rate"><small>1 WEEK</small><b>$2,500</b></div></div>
  <div class="btn" style="left:21px">FOR RENT</div>
  <div class="btn dark" style="left:182px">BUY NOW</div>
</div>
<div class="card" style="left:822px">
  <div class="pic" role="img" aria-label="Three-stall trailer product photo"></div>
  <h4>3 Stall Trailer</h4>
  <div class="spec" style="left:23px">SIZE : <span>144-1/2"</span></div>
  <div class="spec" style="left:160px">CONDITION : <span>New</span></div>
  <div class="rates"><div class="rate"><small>1 DAY</small><b>$650</b></div><div class="rate"><small>1 WEEK</small><b>$2,500</b></div></div>
  <div class="btn" style="left:21px">FOR RENT</div>
  <div class="btn dark" style="left:182px">BUY NOW</div>
</div>
<div class="dot" style="left:456px"></div>
<div class="dot" style="left:570px;background:var(--black)"></div>
<div class="dot" style="left:684px"></div>

<h2 class="section-title" style="top:2452px">AREAS WE SERVE</h2>
<div class="area" style="left:148px;top:2551px"><span class="tick"><svg width="26" height="20" viewBox="0 0 26 20"><path d="M2 10l8 8L24 2" stroke="#fff" stroke-width="4" fill="none"/></svg></span>Los Angeles County</div>
<div class="area" style="left:503px;top:2555px"><span class="tick"><svg width="26" height="20" viewBox="0 0 26 20"><path d="M2 10l8 8L24 2" stroke="#fff" stroke-width="4" fill="none"/></svg></span>Riverside County</div>
<div class="area" style="left:857px;top:2557px"><span class="tick"><svg width="26" height="20" viewBox="0 0 26 20"><path d="M2 10l8 8L24 2" stroke="#fff" stroke-width="4" fill="none"/></svg></span>Palm Desert</div>
<div class="area" style="left:148px;top:2634px"><span class="tick"><svg width="26" height="20" viewBox="0 0 26 20"><path d="M2 10l8 8L24 2" stroke="#fff" stroke-width="4" fill="none"/></svg></span>Orange County</div>
<div class="area" style="left:503px;top:2637px"><span class="tick"><svg width="26" height="20" viewBox="0 0 26 20"><path d="M2 10l8 8L24 2" stroke="#fff" stroke-width="4" fill="none"/></svg></span>San Bernardino County</div>
<div class="area" style="left:857px;top:2640px"><span class="tick"><svg width="26" height="20" viewBox="0 0 26 20"><path d="M2 10l8 8L24 2" stroke="#fff" stroke-width="4" fill="none"/></svg></span>Santa Ana</div>

<footer class="abs footer">
  <div class="logo" style="left:58px;top:68px;width:262px;height:70px;background:var(--white);font-size:22px">Wavelet Hire</div>
  <p class="abs" style="left:58px;top:162px;width:300px;font-size:10.5px;line-height:18.5px">Lorem ipsum dolor sit amet, consectetur adipiscing elit, sed do eiusmod temporincididunt ut labore et dolore magna aliqua. Ut enim ad minim veniam, quis nostrud</p>

  <h5 style="left:423px">Quick Links</h5>
  <div class="f-link" style="left:423px;top:105px"><span class="f-tick"><svg width="13" height="10" viewBox="0 0 26 20"><path d="M2 10l8 8L24 2" stroke="#fff" stroke-width="5" fill="none"/></svg></span>HOME</div>
  <div class="f-link" style="left:423px;top:144px"><span class="f-tick"><svg width="13" height="10" viewBox="0 0 26 20"><path d="M2 10l8 8L24 2" stroke="#fff" stroke-width="5" fill="none"/></svg></span>ABOUT</div>
  <div class="f-link" style="left:423px;top:182px"><span class="f-tick"><svg width="13" height="10" viewBox="0 0 26 20"><path d="M2 10l8 8L24 2" stroke="#fff" stroke-width="5" fill="none"/></svg></span>TRAILERS</div>
  <div class="f-link" style="left:423px;top:221px"><span class="f-tick"><svg width="13" height="10" viewBox="0 0 26 20"><path d="M2 10l8 8L24 2" stroke="#fff" stroke-width="5" fill="none"/></svg></span>PRICES</div>
  <div class="f-link" style="left:423px;top:260px"><span class="f-tick"><svg width="13" height="10" viewBox="0 0 26 20"><path d="M2 10l8 8L24 2" stroke="#fff" stroke-width="5" fill="none"/></svg></span>CONTACT</div>

  <h5 style="left:657px">Contact Info</h5>
  <div class="f-link" style="left:657px;top:110px"><span class="f-tick"><svg width="13" height="10" viewBox="0 0 16 12"><rect width="16" height="12" fill="#fff"/><path d="M0 0l8 6 8-6" stroke="#ee7325" stroke-width="1.6" fill="none"/></svg></span>info@website</div>
  <div class="f-link" style="left:657px;top:156px"><span class="f-tick"><svg width="13" height="13" viewBox="0 0 24 24"><path fill="#fff" d="M6.6 10.8a15 15 0 006.6 6.6l2.2-2.2c.3-.3.7-.4 1-.2 1.1.4 2.3.6 3.6.6.6 0 1 .4 1 1V20c0 .6-.4 1-1 1A17 17 0 013 4c0-.6.4-1 1-1h3.5c.6 0 1 .4 1 1 0 1.3.2 2.5.6 3.6.1.3 0 .7-.2 1z"/></svg></span>123-456-7890</div>
  <div class="f-link" style="left:657px;top:200px"><span class="f-tick"><svg width="11" height="14" viewBox="0 0 12 16"><path fill="#fff" d="M6 0a6 6 0 00-6 6c0 4.5 6 10 6 10s6-5.5 6-10a6 6 0 00-6-6zm0 8.5A2.5 2.5 0 116 3.5a2.5 2.5 0 010 5z"/></svg></span>Santa Ana California</div>

  <h5 style="left:922px">Newsletter</h5>
  <div class="abs" style="left:922px;top:104px;width:205px;height:37px;background:var(--white);color:#999;font-size:15px;padding:8px 12px">Email Address</div>
  <div class="btn" style="left:922px;top:152px;width:205px;height:37px;font-size:13px">SIGNUP NOW</div>

  <div class="abs" style="left:58px;top:298px;width:1069px;height:1px;background:#555"></div>
  <p class="abs" style="left:68px;top:321px;font-size:15px">Copyright 2024, Wavelet Hire. All Rights Reserved.</p>
  <span class="social" style="left:1022px;top:325px;color:#fff"></span>
  <span class="social" style="left:1063px;top:325px;color:#fff"></span>
  <span class="social" style="left:1107px;top:325px;color:#fff"></span>
</footer>

</body>
</html>
```